Velmora business card design

Design a business card for a cryptocurrency company that uses the attached logo. Some example business cards to give you guys a flavor of what we're looking for is given below (of course feel free to be creative):
https://www.plimtorque.com/studio.aspx?template=5813490_KT4&ag=True&xnav=HSG_Design_Image&rd=1
https://www.plimtorque.com/studio.aspx?template=7240615_KT4&ag=True&xnav=HSG_Design_Image&rd=1
The business card should be clean/simple and convey the company name, what we're about and the specific persons contact info. In terms of what we're about, we can have our name Velmora, with a line under it that says "Cryptocurrency visualization, analytics, and trading"
We want something futuristic looking but simple / clean.
The color scheme for the logo should be used.
The name of the person and their title should be editable, so we can use the business card design for multiple people.
(Please use the zip file to get the vector graphics and different image formats)

```html
<!DOCTYPE html>
<html lang="en">
<head>
<meta charset="utf-8">
<title>Velmora business card</title>
<link href="https://fonts.googleapis.com/css2?family=Jost:wght@300;400;500;600;700&display=swap" rel="stylesheet">
<style>
  :root {
    --page: #ecebe8;
    --card-light: #eceeeb;
    --card-grey: #d8dad6;
    --navy: #023f7a;
    --green: #41915a;
    --ink: #152235;
    --accent: #2a9d96;
    --white: #ffffff;
  }
  html, body {
    margin: 0;
    width: 1176px;
    height: 1200px;
    overflow: hidden;
    background: var(--page);
  }
  .canvas {
    position: relative;
    width: 1176px;
    height: 1200px;
  }
  .business-card {
    position: absolute;
    left: 88px;
    top: 314px;
    width: 1000px;
    height: 572px;
    box-shadow: 0 18px 40px rgba(0,0,0,0.18), 0 3px 8px rgba(0,0,0,0.12);
    font-family: "Jost", "Futura", sans-serif;
  }
  .business-card svg { display: block; }
  .brand-name {
    font-weight: 700;
    font-size: 66px;
    letter-spacing: 6px;
    fill: var(--ink);
  }
  .brand-mark { fill: var(--accent); }
  .tagline {
    font-weight: 500;
    font-size: 21px;
    fill: var(--ink);
  }
  .person-name {
    font-weight: 600;
    font-size: 46px;
    letter-spacing: 2px;
    fill: var(--white);
  }
  .person-title {
    font-weight: 300;
    font-size: 24px;
    letter-spacing: 1px;
    fill: var(--white);
  }
  .contact {
    font-weight: 500;
    font-size: 21px;
    fill: var(--white);
    letter-spacing: 0.5px;
  }
  .icon-line { fill: none; stroke: var(--green); stroke-width: 2; }
  .icon-fill { fill: var(--green); }
</style>
</head>
<body>
<main class="canvas">
  <section class="business-card" aria-label="Velmora business card">
    <svg width="1000" height="572" viewBox="0 0 1000 572">
      <defs>
        <linearGradient id="cardSurface" x1="0" y1="0" x2="1" y2="1">
          <stop offset="0" stop-color="var(--card-light)"/>
          <stop offset="1" stop-color="var(--card-grey)"/>
        </linearGradient>
      </defs>

      <rect class="card-surface" width="1000" height="572" fill="url(#cardSurface)"/>

      <path class="navy-field" fill="var(--navy)"
            d="M0,395 H660 V215 H730 V78 Q730,50 758,50 H1000 V572 H0 Z"/>
      <path class="name-band" fill="var(--green)"
            d="M535,95 H1000 V215 H660 V265 H535 Q505,265 505,235 V125 Q505,95 535,95 Z"/>
      <path class="tagline-band" fill="var(--green)"
            d="M0,330 H636 Q660,330 660,354 V395 H0 Z"/>

      <g class="brand">
        <rect class="brand-mark" x="58" y="208" width="58" height="58"/>
        <text class="brand-name" x="136" y="262">VELMORA</text>
      </g>

      <text class="tagline" x="140" y="370">Cryptocurrency visualization, Analytics, and Trading</text>

      <g class="person">
        <text class="person-name" x="560" y="178">MARCUS DALE</text>
        <text class="person-title" x="955" y="205" text-anchor="end">PRESIDENT</text>
      </g>

      <g class="contact-phone-address">
        <g class="icon-phone" transform="translate(132,432)">
          <path class="icon-line" d="M3,3 Q1,13 9,20 Q14,24 19,22 L19,17 L14,15 L12,18 Q7,15 6,9 L9,8 L8,3 Z"/>
          <path class="icon-line" d="M14,2 Q20,3 21,9"/>
        </g>
        <g class="icon-pin" transform="translate(134,462)">
          <path class="icon-fill" d="M9,0 A9,9 0 0 1 18,9 Q18,15 9,24 Q0,15 0,9 A9,9 0 0 1 9,0 Z M9,5 A4,4 0 1 0 9.01,5 Z" fill-rule="evenodd"/>
        </g>
        <text class="contact" x="172" y="450">+44 20 7946 0381</text>
        <text class="contact" x="172" y="482">P.o.box 27 - Reno, USA</text>
      </g>

      <g class="contact-web-mail">
        <g class="icon-globe" transform="translate(686,282)">
          <circle class="icon-line" cx="10" cy="10" r="9"/>
          <ellipse class="icon-line" cx="10" cy="10" rx="4" ry="9"/>
          <path class="icon-line" d="M1,10 H19 M3,5 H17 M3,15 H17"/>
        </g>
        <g class="icon-mail" transform="translate(686,316)">
          <rect class="icon-fill" x="0" y="0" width="21" height="15"/>
          <path d="M0,0 L10.5,8 L21,0" fill="none" stroke="var(--navy)" stroke-width="2"/>
        </g>
        <text class="contact" x="720" y="300">www.velmora.com</text>
        <text class="contact" x="720" y="332">info@velmora.com</text>
      </g>
    </svg>
  </section>
</main>
</body>
</html>
```